Business Card Velostra - Accounting firm

Hi my friend.
I'm coming back to you to see if it would be possible for you to make a modern and minimalist business card design.
In shades of blue like the great logo you offered me.
The ideal is a modern and aesthetic business card.
The goal is to give a professional effect to the first exchanges.
Renewal and innovation in the accounting world !!
I thank you !!
Good evening to you

Target Market(s)

Young, dynamic and sensitive to marketing

Industry/Entity Type

Finance And Accounting

Contact Information for Business Card

Company logo and name. Last name, First name, Phone number, email address, company address, website.

Font styles to use
Sans Serif

Requirements
Must have
• The ideal is a modern and aesthetic business card.

Mentions to include: Company logo and name. Last name, First name, Phone number, email address, company address, website.
Nice to have
• The goal is to give a professional effect to the first exchanges.
Should not have
• Simplistic or childish design

```html
<!DOCTYPE html>
<html lang="en">
<head>
<meta charset="utf-8">
<title>Velostra Business Card</title>
<link rel="stylesheet" href="https://fonts.googleapis.com/css2?family=Arimo:wght@400;700&display=swap">
<style>
  :root {
    --backdrop: #1c1c1e;
    --navy: #06256a;
    --navy-deep: #041c52;
    --teal: #3cc9b8;
    --azure: #1a7fd0;
    --white: #ffffff;
  }
  * { margin: 0; padding: 0; box-sizing: border-box; }
  html, body {
    width: 1200px; height: 1015px; overflow: hidden;
    background: radial-gradient(ellipse at center, #3a3a3c 0%, var(--backdrop) 75%);
    font-family: "Arimo", Arial, sans-serif;
  }
  .sheet {
    position: relative; width: 1200px; height: 1015px;
    display: flex; flex-direction: column; align-items: center; justify-content: center; gap: 70px;
  }
  .card {
    position: relative; width: 600px; height: 343px; overflow: hidden;
    background: var(--navy);
    box-shadow: 0 18px 40px rgba(0,0,0,.55);
  }
  /* Front */
  .card--front { display: flex; align-items: center; justify-content: center; }
  .brand { display: flex; align-items: center; gap: 16px; }
  .brand__dot { width: 44px; height: 44px; border-radius: 50%; background: var(--teal); }
  .brand__name { font-weight: 700; font-size: 64px; letter-spacing: -1px; color: var(--white); }
  /* Back */
  .card__emblem { position: absolute; inset: 0; }
  .card__brand {
    position: absolute; right: 40px; top: 122px;
    display: flex; align-items: center; gap: 10px;
  }
  .card__brand .brand__dot { width: 30px; height: 30px; background: var(--navy); }
  .card__brand .brand__name { font-size: 46px; color: var(--navy); }
  .contact {
    position: absolute; left: 48px; top: 118px; color: var(--white);
  }
  .contact__name { font-weight: 700; font-size: 22px; color: var(--teal); letter-spacing: .3px; white-space: nowrap; }
  .contact__role { font-size: 18px; margin-top: 2px; }
  .contact__address { font-size: 18px; line-height: 1.2; margin-top: 22px; }
  .contact__list { list-style: none; margin-top: 18px; font-size: 18px; }
  .contact__list li { display: flex; align-items: center; gap: 10px; line-height: 1.3; }
  .contact__list svg { width: 17px; height: 17px; flex: none; }
</style>
</head>
<body>
<main class="sheet">
  <section class="card card--front" aria-label="Card front">
    <div class="brand">
      <span class="brand__dot"></span>
      <span class="brand__name">velostra</span>
    </div>
  </section>

  <section class="card card--back" aria-label="Card back">
    <svg class="card__emblem" viewBox="0 0 600 343" aria-hidden="true">
      <defs>
        <linearGradient id="ring" x1="0" y1="0" x2="1" y2="1">
          <stop offset="0" stop-color="#3cc9b8"/>
          <stop offset="1" stop-color="#1a7fd0"/>
        </linearGradient>
      </defs>
      <circle cx="492" cy="114" r="202" fill="url(#ring)"/>
      <circle cx="501" cy="107" r="202" fill="#06256a"/>
      <circle cx="505" cy="103" r="200" fill="#ffffff"/>
    </svg>

    <div class="card__brand">
      <span class="brand__dot"></span>
      <span class="brand__name">velostra</span>
    </div>

    <div class="contact">
      <p class="contact__name">MARCUS DELAINE</p>
      <p class="contact__role">Managing Director</p>
      <p class="contact__address">78 Harbor Lane,<br>Lyon, 69002</p>
      <ul class="contact__list">
        <li>
          <svg viewBox="0 0 24 24"><path fill="#3cc9b8" d="M6.6 10.8a15 15 0 0 0 6.6 6.6l2.2-2.2a1 1 0 0 1 1-.25 11.4 11.4 0 0 0 3.6.57 1 1 0 0 1 1 1V20a1 1 0 0 1-1 1A17 17 0 0 1 3 4a1 1 0 0 1 1-1h3.5a1 1 0 0 1 1 1c0 1.25.2 2.45.57 3.57a1 1 0 0 1-.25 1z"/></svg>
          044-987 210 635
        </li>
        <li>
          <svg viewBox="0 0 24 24"><path fill="#3cc9b8" d="M2 5h20v14H2zm2 2v.5l8 5 8-5V7zm0 2.8V17h16V9.8l-8 5z"/></svg>
          hello@velostra.com
        </li>
        <li>
          <svg viewBox="0 0 24 24"><circle cx="12" cy="12" r="9" fill="none" stroke="#3cc9b8" stroke-width="2"/><path d="M3 12h18M12 3c3 3 3 15 0 18M12 3c-3 3-3 15 0 18" fill="none" stroke="#3cc9b8" stroke-width="1.6"/></svg>
          www.velostra.com
        </li>
      </ul>
    </div>
  </section>
</main>
</body>
</html>
```